KerrLow Farm

Need a nice simple clean double sided business card that has our logo and info on:
Kerr Low Farm
Martin & Felicity Kerr Low
kerrlowfarm@mailbarn.example
Martin: 1-780-555-0148
Felicity: 1-780-555-0193
Instagram @ kerrlow_farm

Contact Information for Business Card

Martin & Felicity Kerr Low kerrlowfarm@mailbarn.example Martin: 1-780-555-0148 Felicity: 1-780-555-0193

```html
<!DOCTYPE html>
<html lang="en">
<head>
<meta charset="utf-8">
<title>Kerr Low Farm — Business Card</title>
<link rel="stylesheet" href="https://fonts.googleapis.com/css2?family=Libre+Baskerville:wght@700&family=Arimo:wght@400&display=swap">
<style>
  :root {
    --backdrop: #9c9c9c;
    --card-dark: #231f20;
    --card-light: #ffffff;
    --green: #5d9e12;
    --orange: #f5a20c;
    --ink: #3f3f3f;
  }
  * { margin: 0; padding: 0; box-sizing: border-box; }
  html, body { width: 1200px; height: 1200px; overflow: hidden; }
  body {
    background: var(--backdrop);
    position: relative;
    font-family: "Arimo", Helvetica, Arial, sans-serif;
  }
  .card {
    position: absolute;
    top: 303px;
    width: 368px;
    height: 594px;
    box-shadow: 3px 4px 6px rgba(0,0,0,0.45);
    text-align: center;
  }
  .card--front { left: 200px; background: var(--card-dark); }
  .card--back { left: 599px; background: var(--card-light); }

  .brand {
    position: absolute; left: 0; right: 0;
    display: flex; justify-content: center; align-items: center; gap: 12px;
  }
  .brand__square {
    width: 16px; height: 16px;
    background: var(--orange);
    flex: none;
  }
  .brand__name {
    font-family: "Arimo", Helvetica, Arial, sans-serif;
    font-weight: 400;
    font-size: 30px;
    color: var(--green);
    white-space: nowrap;
  }
  .card--front .brand { top: 470px; }
  .card--back .brand { top: 190px; }

  .owners {
    position: absolute; top: 370px; left: 0; right: 0;
    font-family: "Libre Baskerville", Georgia, serif;
    font-weight: 700;
    font-size: 16.5px;
    color: var(--green);
    text-transform: uppercase;
    white-space: nowrap;
    letter-spacing: -0.3px;
  }
  .contact-icons {
    position: absolute; top: 404px; left: 0; right: 0;
    display: flex; justify-content: center; align-items: center; gap: 6px;
  }
  .contact-icons__rule { width: 32px; height: 1px; background: var(--ink); margin: 0 2px; }
  .contact-icons svg { width: 25px; height: 25px; display: block; }
  .contact-list {
    position: absolute; top: 443px; left: 0; right: 0;
    list-style: none;
    font-size: 17px;
    line-height: 27.3px;
    color: var(--ink);
    white-space: nowrap;
  }
  .contact-list__label { color: var(--orange); }
</style>
</head>
<body>
  <section class="card card--front">
    <div class="brand">
      <span class="brand__square"></span>
      <p class="brand__name">Kerr Low Farm</p>
    </div>
  </section>

  <section class="card card--back">
    <div class="brand">
      <span class="brand__square"></span>
      <p class="brand__name">Kerr Low Farm</p>
    </div>

    <p class="owners">Martin &amp; Felicity Kerr Low</p>

    <div class="contact-icons">
      <span class="contact-icons__rule"></span>
      <svg viewBox="0 0 26 26" aria-label="Phone">
        <circle cx="13" cy="13" r="11.5" fill="none" stroke="#5d9e12" stroke-width="1.6"/>
        <path d="M9 7.5c-1.2.8-1.6 2-1 3.6 1.2 3 3.6 5.6 6.6 6.9 1.5.6 2.8.3 3.6-.9l-2.2-2-1.3.9c-1.4-.7-2.6-2-3.3-3.4l.9-1.3z" fill="#5d9e12"/>
      </svg>
      <svg viewBox="0 0 26 26" aria-label="Phone">
        <circle cx="13" cy="13" r="11.5" fill="none" stroke="#5d9e12" stroke-width="1.6"/>
        <path d="M9 7.5c-1.2.8-1.6 2-1 3.6 1.2 3 3.6 5.6 6.6 6.9 1.5.6 2.8.3 3.6-.9l-2.2-2-1.3.9c-1.4-.7-2.6-2-3.3-3.4l.9-1.3z" fill="#5d9e12"/>
      </svg>
      <svg viewBox="0 0 26 26" aria-label="Email">
        <circle cx="13" cy="13" r="11.5" fill="none" stroke="#5d9e12" stroke-width="1.6"/>
        <rect x="6.5" y="8.5" width="13" height="9" fill="#5d9e12"/>
        <path d="M6.5 8.5l6.5 5 6.5-5" fill="none" stroke="#fff" stroke-width="1"/>
      </svg>
      <svg viewBox="0 0 26 26" aria-label="Social profile">
        <circle cx="13" cy="13" r="11.5" fill="none" stroke="#5d9e12" stroke-width="1.6"/>
        <circle cx="13" cy="13" r="5" fill="#5d9e12"/>
      </svg>
      <span class="contact-icons__rule"></span>
    </div>

    <ul class="contact-list">
      <li><span class="contact-list__label">Martin:</span> 1-780-555-0148</li>
      <li><span class="contact-list__label">Felicity:</span> 1-780-555-0193</li>
      <li>kerrlowfarm@mailbarn.example</li>
      <li>@kerrlow_farm</li>
    </ul>
  </section>
</body>
</html>
```